Fundraising Study Day East of England. Lift the January blues!

A flyer to advertise a fundraising event of lectures for dental hygienists and therapists in support of the exemption campaign. Currently dental hygienists and therapists require a prescription to deliver certain treatment or recommend certain toothpastes. If we are successful in the campaign we will be able to treat patients without these restrictions.

Industry/Entity Type

Dental

```html
<!DOCTYPE html>
<html lang="en">
<head>
<meta charset="utf-8">
<title>Fundraising Study Day – East of England</title>
<link rel="stylesheet" href="https://fonts.googleapis.com/css2?family=Oswald:wght@600&family=Courgette&family=Arimo&family=Lato:wght@400;700;900&display=swap">
<style>
:root{
  --navy:#1f3c88;
  --teal:#00a7cc;
  --red:#e3222b;
  --yellow:#ffe600;
  --orange:#f26522;
  --ink:#3a3a3a;
  --page:#f3f5f8;
}
*{margin:0;padding:0;box-sizing:border-box}
html,body{width:998px;height:1200px;overflow:hidden;background:#fff}
.poster{position:relative;width:998px;height:1200px;overflow:hidden;
  background:linear-gradient(180deg,#fff 0%,var(--page) 60%,#e9edf2 100%);
  font-family:"Lato",sans-serif;color:var(--ink)}
.hero-photo{position:absolute;left:0;top:0;width:998px;height:580px;
  background:
    linear-gradient(180deg,rgba(255,255,255,0) 55%,rgba(255,255,255,.9) 100%),
    radial-gradient(ellipse at 80% 62%,#2bb3c6 0 14%,transparent 15%),
    radial-gradient(ellipse at 58% 40%,#f4f6f8 0 16%,transparent 17%),
    radial-gradient(ellipse at 46% 34%,#9cc3e3 0 11%,transparent 12%),
    radial-gradient(ellipse at 34% 42%,#f7f7f7 0 11%,transparent 12%),
    linear-gradient(90deg,#e8eef2 0%,#dfe7ec 40%,#eef2f4 100%)}
.title-block{position:absolute;left:80px;top:262px}
.title-main{font-family:"Oswald",sans-serif;font-weight:600;font-size:46px;color:var(--navy);letter-spacing:.5px;line-height:1.1}
.title-region{font-family:"Courgette",cursive;font-size:40px;color:var(--red);line-height:1.15}
.title-tagline{font-family:"Arimo",sans-serif;font-size:36px;color:#3b3b3b;line-height:1.2}
.description{position:absolute;left:70px;top:434px;width:870px;height:150px}
.description svg{position:absolute;inset:0}
.description-tab{position:absolute;left:30px;top:6px;height:36px;padding:0 24px;line-height:36px;
  background:var(--navy);color:var(--yellow);font-weight:900;font-size:17px;letter-spacing:.5px}
.description-text{position:absolute;left:48px;top:56px;width:760px;color:#fff;font-size:14px;line-height:1.4}
.agenda{position:absolute;left:70px;top:614px;width:560px}
.agenda-heading{display:flex;align-items:center;gap:8px;color:var(--red);font-weight:900;font-size:26px;margin-left:20px;margin-bottom:6px}
.session{margin-left:30px;margin-bottom:6px;font-size:13px;line-height:1.3}
.session-time{display:flex;align-items:center;gap:6px;color:var(--navy);font-weight:900;font-size:15px}
.session p b{color:#222}
.break-bar{display:inline-block;background:var(--teal);color:var(--yellow);font-weight:900;font-size:14px;
  padding:3px 14px 3px 44px;margin:2px 0 6px -10px;clip-path:polygon(0 0,100% 0,96% 100%,0 100%)}
.break-bar span{color:#fff;margin-left:6px}
.venue-card{position:absolute;left:680px;top:620px;width:250px;height:440px;background:#fff;
  border:3px solid var(--navy);border-radius:12px;overflow:hidden;box-shadow:0 4px 12px rgba(0,0,0,.15)}
.card-label{display:inline-block;background:var(--teal);color:var(--yellow);font-weight:900;font-size:14px;padding:3px 14px;margin-top:14px}
.venue-address{font-size:13px;padding:8px 16px 6px;line-height:1.35}
.venue-map{margin:4px 16px;height:160px;background:linear-gradient(135deg,#eef1ec,#e3e8e0 50%,#cfe3c3);border:1px solid #ccc;position:relative}
.venue-map svg{position:absolute;left:50%;top:40%;transform:translate(-50%,-50%)}
.event-date{font-size:13px;padding:6px 16px;line-height:1.6}
.event-date em{font-style:normal;color:var(--orange)}
.cost{position:absolute;left:0;bottom:0;width:100%;height:62px;background:var(--navy);color:var(--yellow);
  font-weight:900;font-size:28px;text-align:center;line-height:62px}
.footer{position:absolute;left:0;top:1110px;width:998px;height:70px;background:var(--navy);
  display:flex;align-items:center;padding-left:90px;gap:8px;font-size:14px;color:#fff}
.footer b{color:var(--yellow)}
</style>
</head>
<body>
<main class="poster">
  <div class="hero-photo" role="img" aria-label="Photo of four smiling dental professionals in scrubs and white coats standing in a bright dental surgery"></div>

  <header class="title-block">
    <h1 class="title-main">FUNDRAISING STUDY DAY</h1>
    <p class="title-region">East of England.</p>
    <p class="title-tagline">Lift the January blues!</p>
  </header>

  <section class="description">
    <svg width="870" height="150" viewBox="0 0 870 150">
      <path d="M20 28 H860 Q872 28 868 42 L850 130 Q846 146 830 146 H40 Q22 146 20 130 L8 48 Q6 30 20 28Z" fill="var(--teal)"/>
      <path d="M868 42 L850 130 Q846 146 830 146 H40" fill="none" stroke="var(--yellow)" stroke-width="2.5"/>
    </svg>
    <div class="description-tab">DESCRIPTION</div>
    <p class="description-text">A fundraising event to support our exemptions project. The day will consist of a series of presentations ranging from the new ECPD to new technologies. The aim, being to enhance our learning and raise funds to support the exemptions campaign. The speaker line includes some of the UK and Irelands most respected dental professionals in our field.</p>
  </section>

  <section class="agenda">
    <h2 class="agenda-heading">
      <svg width="24" height="24" viewBox="0 0 24 24"><circle cx="12" cy="12" r="11" fill="none" stroke="var(--red)" stroke-width="1.5"/><rect x="6" y="7" width="12" height="11" rx="1" fill="none" stroke="var(--red)" stroke-width="1.5"/><line x1="6" y1="10" x2="18" y2="10" stroke="var(--red)" stroke-width="1.5"/></svg>
      AGENDA
    </h2>
    <div class="session">
      <div class="session-time"><svg width="12" height="12" viewBox="0 0 12 12"><circle cx="6" cy="6" r="5" fill="none" stroke="#333"/><path d="M6 3V6H8.5" fill="none" stroke="#333"/></svg>9.30 - 10.15</div>
      <p><b>Hannah Lowell:</b> Immediate past president of the AHTP will be updating us on all things ECPD</p>
    </div>
    <div class="session">
      <div class="session-time"><svg width="12" height="12" viewBox="0 0 12 12"><circle cx="6" cy="6" r="5" fill="none" stroke="#333"/><path d="M6 3V6H8.5" fill="none" stroke="#333"/></svg>10.15 - 11.00</div>
      <p><b>Tessa Marlow:</b> Will provide an update on teeth whitening and explain how social media has impacted her business.</p>
      <p><b>Clara Benning:</b> Our internationally acclaimed speaker will update our knowledge of periodontal disease and nutrition and new technologies.</p>
    </div>
    <div class="break-bar">11.00 - 11.30 <span>BREAK</span></div>
    <div class="session">
      <div class="session-time"><svg width="12" height="12" viewBox="0 0 12 12"><circle cx="6" cy="6" r="5" fill="none" stroke="#333"/><path d="M6 3V6H8.5" fill="none" stroke="#333"/></svg>11.30 - 13.00</div>
      <p><b>Niamh Carrow &amp; Rosalind Hatch:</b> Will be providing a combined presentation on 'Scaling your business' and start to finish Sonara techniques. The aim being to build our business with effective communications, systems and protocols. This sessions promises audience participation!</p>
    </div>
    <div class="break-bar">12 - 14.00 <span>LUNCH</span></div>
    <div class="session">
      <div class="session-time"><svg width="12" height="12" viewBox="0 0 12 12"><circle cx="6" cy="6" r="5" fill="none" stroke="#333"/><path d="M6 3V6H8.5" fill="none" stroke="#333"/></svg>14 - 15.00</div>
      <p><b>Priya Desai:</b> Save your back. All things posture.</p>
    </div>
    <div class="break-bar">15.00 - 15.30 <span>BREAK</span></div>
    <div class="session">
      <div class="session-time"><svg width="12" height="12" viewBox="0 0 12 12"><circle cx="6" cy="6" r="5" fill="none" stroke="#333"/><path d="M6 3V6H8.5" fill="none" stroke="#333"/></svg>15.30 - 16.30</div>
      <p><b>Clara Benning:</b> Our internationally acclaimed speaker will update our knowledge of periodontal disease and nutrition and new technologies.</p>
    </div>
  </section>

  <aside class="venue-card">
    <span class="card-label">LOCATION</span>
    <p class="venue-address">Larkfield Hotel Meridian Way Fenbridge FB4 2QT</p>
    <div class="venue-map" role="img" aria-label="Street map of the area around the venue with a location marker">
      <svg width="18" height="24" viewBox="0 0 18 24"><path d="M9 0C4 0 0 4 0 9c0 6 9 15 9 15s9-9 9-15c0-5-4-9-9-9z" fill="var(--orange)"/><circle cx="9" cy="9" r="3" fill="#fff"/></svg>
    </div>
    <span class="card-label">DATE AND TIME</span>
    <p class="event-date">Fri, <em>19 January</em> 2018<br>09:00 – 16:30 GMT</p>
    <div class="cost">Cost - £101.48</div>
  </aside>

  <footer class="footer">
    <svg width="16" height="16" viewBox="0 0 16 16"><circle cx="8" cy="8" r="7" fill="none" stroke="var(--yellow)" stroke-width="1.5"/><ellipse cx="8" cy="8" rx="3" ry="7" fill="none" stroke="var(--yellow)" stroke-width="1.2"/><line x1="1" y1="8" x2="15" y2="8" stroke="var(--yellow)" stroke-width="1.2"/></svg>
    <b>Visit Us:</b> www.ticketfold.co.uk/e/fundraising-study-day-east-of-england-lift-the-january-blues-tickets-50218874316
  </footer>
</main>
</body>
</html>
```